Business card with professional look

I would like a creative yet professional looking business card for our business. We sell broadcast TV related security products for mobile phones, set top boxes, and tablets. Our customers are international. We have a logo we like and I would like to possibly add some color to the business card but keep it professional looking.

Target Market(s)

Professionals in the TV, cable, ans Satellite industries

Industry/Entity Type

Cable Tv

Contact Information for Business Card

Name Ned Vastermill, title CEO, Address 8130 Harborline Court, Suite 400, Del Arvo, CA 91584 USA, phone numbers m:+1.619.284.7302 o:+1.855.672.9140, email, logo

Font styles to use
Other font styles liked:
• Open to any font that looks good with logo

Requirements
Must have
• professional look with colors coordinated with logo colors. would like to add one or two different colors as well as some form of background color

```html
<!DOCTYPE html>
<html lang="en">
<head>
<meta charset="utf-8">
<title>Vantoral – Business Card</title>
<link href="https://fonts.googleapis.com/css2?family=Open+Sans:wght@400;600;700&display=swap" rel="stylesheet">
<style>
  :root {
    --page-bg: #e9e7e3;
    --card-top: #ffffff;
    --card-bottom: #f1f1f1;
    --brand-blue: #1f63b5;
    --accent-blue: #3a9ad9;
    --ink: #3b3b3b;
    --ink-soft: #555555;
    --logo-grey: #5c5c5c;
  }
  * { margin: 0; padding: 0; box-sizing: border-box; }
  html, body {
    width: 1200px;
    height: 1022px;
    overflow: hidden;
    background: var(--page-bg);
    font-family: "Open Sans", Arial, sans-serif;
  }
  .stage {
    width: 1200px;
    height: 1022px;
    display: flex;
    align-items: center;
    justify-content: center;
  }
  .card {
    position: relative;
    width: 1000px;
    height: 572px;
    border-radius: 22px;
    background: linear-gradient(160deg, var(--card-top) 0%, var(--card-bottom) 100%);
    box-shadow: 0 14px 40px rgba(0,0,0,0.18);
    display: flex;
    align-items: center;
    padding: 0 80px;
  }
  .brand {
    display: flex;
    align-items: center;
    gap: 18px;
    width: 470px;
  }
  .brand-mark {
    width: 58px;
    height: 58px;
    border-radius: 8px;
    background: linear-gradient(180deg, var(--accent-blue), var(--brand-blue));
  }
  .brand-name {
    font-size: 66px;
    font-weight: 700;
    color: var(--logo-grey);
    letter-spacing: -1px;
  }
  .contact {
    color: var(--ink);
  }
  .contact-name {
    font-size: 36px;
    font-weight: 700;
    color: var(--brand-blue);
    line-height: 1.1;
  }
  .contact-title {
    font-size: 22px;
    color: var(--ink-soft);
    margin-bottom: 26px;
  }
  .address {
    font-size: 23px;
    line-height: 1.3;
    margin-bottom: 24px;
  }
  .lines { list-style: none; }
  .lines li {
    display: flex;
    align-items: center;
    gap: 12px;
    font-size: 23px;
    line-height: 1.35;
  }
  .lines svg { width: 16px; height: 16px; flex: none; }
  .email-domain { color: var(--brand-blue); }
</style>
</head>
<body>
<main class="stage">
  <section class="card">
    <div class="brand">
      <span class="brand-mark"></span>
      <span class="brand-name">Vantoral</span>
    </div>
    <div class="contact">
      <h1 class="contact-name">Ned Vastermill</h1>
      <p class="contact-title">CEO</p>
      <p class="address">8130 Harborline Court,<br>Suite 400, Del Arvo<br>CA 91584 USA</p>
      <ul class="lines">
        <li>
          <svg viewBox="0 0 16 16" aria-hidden="true"><rect x="4" y="1" width="8" height="14" rx="1.5" fill="none" stroke="#1f63b5" stroke-width="1.6"/><rect x="6" y="11.5" width="4" height="1.4" fill="#1f63b5"/></svg>
          +1.619.284.7302
        </li>
        <li>
          <svg viewBox="0 0 16 16" aria-hidden="true"><path d="M4 1.5 L6.5 4.5 L5 6.5 C6 8.5 7.5 10 9.5 11 L11.5 9.5 L14.5 12 L12.5 14.5 C7 14 2 9 1.5 3.5 Z" fill="#1f63b5"/></svg>
          +1.855.672.9140
        </li>
        <li>
          <svg viewBox="0 0 16 16" aria-hidden="true"><rect x="1.5" y="3" width="13" height="10" fill="none" stroke="#1f63b5" stroke-width="1.6"/><path d="M1.5 3 L8 9 L14.5 3" fill="none" stroke="#1f63b5" stroke-width="1.6"/></svg>
          <span>info@<span class="email-domain">vantoral</span>.com</span>
        </li>
      </ul>
    </div>
  </section>
</main>
</body>
</html>
```